Tarrow Consulting Needs Standardised Stationery!

Hello,I am looking at having some standardised stationery to continue building my brand. I am looking for a relatively clean and simple designs using the colours from my logos. Tarrow Consulting is the main business with Career Beacon Australia a subsidiary.
In particular I am after a design for:
- Letterhead (very important), white background, professional, corporate that I can send to prospective clients. Logo colours.
- Envelope, standard design I can print onto envelopes.
- Pens
- Other stationery/promotional items I can create

Target Market(s)

Universities, government, large organisations.

Industry/Entity Type

Professional Service

Font styles to use
Serif

Requirements
Must have
• Logo, match the design of the Tarrow Consulting logo. Black Career Beacon Australia logo is a subsidiary.
Should not have
• Too much colour, some colour is good, but I am looking for a clean professional look.

```html
<!DOCTYPE html>
<html lang="en">
<head>
<meta charset="utf-8">
<title>Tarrow Consulting Letterhead</title>
<link rel="stylesheet" href="https://fonts.googleapis.com/css2?family=Lato:wght@400;700&family=Yellowtail&display=swap">
<style>
  :root{
    --backdrop:#d6d6d6;
    --paper:#ffffff;
    --ink:#2b2b2b;
    --body:#5a5a5a;
    --blue:#1a8ccc;
    --green:#1caf55;
    --orange:#e2843a;
    --rule:#bdbdbd;
  }
  *{margin:0;padding:0;box-sizing:border-box}
  html,body{width:1200px;height:1113px;overflow:hidden;background:var(--backdrop)}
  body{position:relative;font-family:"Lato",sans-serif}
  .letterhead{position:absolute;left:291px;top:119px;width:617px;height:875px;background:var(--paper);overflow:hidden;box-shadow:0 6px 22px rgba(0,0,0,.18)}
  .brand{position:absolute;left:44px;top:34px;font-size:21px;line-height:24px;font-weight:700;color:var(--ink);letter-spacing:.3px}
  .address{position:absolute;left:462px;top:34px;padding-left:5px;border-left:1px solid var(--rule);font-size:9.5px;line-height:13px;color:var(--ink)}
  .letter{position:absolute;left:44px;top:252px;width:528px}
  .salutation{font-size:11.5px;line-height:16px;font-weight:700;color:var(--blue);margin-bottom:16px}
  .letter p.body{font-size:11.5px;line-height:18.7px;color:var(--body);text-align:justify;hyphens:auto;-webkit-hyphens:auto;margin-bottom:14px}
  .closing{font-size:14.5px;line-height:18px;color:var(--ink);margin-top:18px}
  .signature{font-family:"Yellowtail",cursive;font-size:25px;line-height:30px;color:var(--blue);margin-top:2px}
  .subsidiary{position:absolute;left:150px;top:788px;display:flex;align-items:center;gap:5px}
  .subsidiary-dot{width:28px;height:28px;border-radius:50%;background:var(--ink)}
  .subsidiary-name{font-size:8.5px;line-height:10.5px;font-weight:700;color:var(--ink)}
  .footer-band{position:absolute;left:0;right:0;bottom:0;height:48px;background:var(--green);border-top:3px solid var(--blue)}
  .contact{position:absolute;left:0;right:0;bottom:11px;display:flex;justify-content:center;gap:8px;font-size:9.7px;line-height:12px;color:#fff}
  .contact span{display:flex;align-items:center;gap:3px}
  .contact svg{width:7px;height:7px}
</style>
</head>
<body>
  <main class="letterhead">
    <div class="brand">Tarrow Consulting</div>
    <div class="address">Street Name, City Name<br>Zicode - 012345</div>

    <section class="letter">
      <p class="salutation">Dear Mr. Lorem,</p>
      <p class="body">Lorem ipsum dolor sit amet, consectetuer adipiscing elit, sed diam nonummy nibh euismod tincidunt ut laoreet dolore magna aliquam erat volutpat. Ut wisi enim ad minim veniam, quis nostrud exerci tation ullamcorper suscipit lobortis nisl ut aliquip ex ea commodo consequat. Duis autem vel eum iriure dolor in hendiusto odio dignissim qui blandit praesent luptatum zzril delenit augue duis dolore te feugait nulla facilisi.</p>
      <p class="body">Lorem ipsum dolor sit amet, consectetuer adipiscing elit, sed diam nonummy nibh euismod tincidunt ut laoreet dolore magna aliquam erat volutpat. Ut wisi enim ad minim veniam, quis nostrud exerci tation ullamcorper suscipit lobortis nisl ut aliquip ex ea commodo consequat. Duis autem vel eum iriure dolor in hendiusto odio dignissim qui blandit praesent luptatum zzril delenit augue duis dolore te feugait nulla facilisi.</p>
      <p class="body">Lorem ipsum dolor sit amet, consectetuer adipiscing elit, sed diam nonummy nibh euismod tincidunt ut laoreet dolore magna aliquam erat volutpat. Ut wisi enim ad minim veniam, quis nostrud exerci tation ullamcorper suscipit lobortis nisl ut aliquip ex ea commodo consequat. Duis autem vel eum iriure dolor in hendiusto odio dignissim qui blandit praesent luptatum zzril delenit augue duis dolore te feugait nulla facilisi.</p>
      <p class="closing">Sincerely Your,</p>
      <p class="signature">Your Name</p>
    </section>

    <div class="subsidiary">
      <span class="subsidiary-dot"></span>
      <span class="subsidiary-name">Career<br>Beacon<br>Australia</span>
    </div>

    <footer class="footer-band"></footer>
    <div class="contact">
      <span><svg viewBox="0 0 10 10"><path fill="#fff" d="M2 0.5 L3.6 2.6 L2.8 3.6 C3.4 5 4.8 6.4 6.4 7.2 L7.4 6.4 L9.5 8 L8.4 9.5 C4.5 9 1 5.5 0.5 1.6Z"/></svg>012-345-6789</span>
      <span><svg viewBox="0 0 10 10"><rect x="0.5" y="2" width="9" height="6.5" fill="#fff"/><path d="M0.5 2 L5 5.6 L9.5 2" stroke="#1caf55" stroke-width="0.9" fill="none"/></svg>sales@tarrowconsulting.com</span>
      <span><svg viewBox="0 0 10 10" fill="none" stroke="#fff" stroke-width="0.9"><circle cx="5" cy="5" r="4.3"/><ellipse cx="5" cy="5" rx="2" ry="4.3"/><path d="M0.7 5 H9.3"/></svg>www.tarrowconsulting.com</span>
    </div>
  </main>
</body>
</html>
```